Private Maths Tuition Flyer based in London

I am opening up a new Maths tuition centre in North West London. The flyer will be delivered to over 8,000 homes within the immediate vicinity. The design should be suitable to be printed on an A5 sheet and read in a portrait orientation.

The flyer should include the following:

The headline statement should be "Private Maths Tuition"

Secondary headline statement is the following "GCSE, A-Levels, 11 Plus exams"

Some of service offerings/selling points are:

- Free first session
- Monthly Feedback reports
- Free support outside of sessions
- Clear Target grades
- Personalised Lesson plans
- Tangible Results

Another statement that should be featured is "Book your free session by visiting www.lernova.co.uk" or something similar to that.

"Contact Details:
020 7418 2903
enquiries@lernova.co.uk"

"Address:
Corbel Business and Innovation Centre
Wyvern Court
Larkfield Road
HA9 4QW"

Attached you'll see a logo which should be included and also a map of where we are. I am open to new images for the map if you guys have any, rather than a screen shot from plotway atlas but it should be clear to see.

I would like the content above to be displayed in a clear and concise manner that is easy to read. You have creative license on where this information should be displayed and where the images should be but on the whole it should look aesthetically pleasing on the eye.

Target Market(s)

Students, Parents. Parents who want maths tutors.

Industry/Entity Type

Tutoring

Font styles to use
Sans Serif

Requirements
Must have
• *logo*
• Private Maths Tuition
• GCSE, A-Levels, 11 Plus exams
• - Free first session
• - Monthly Feedback reports
• - Free support outside of sessions
• - Clear Target grades
• - Personalised Lesson plans
• - Tangible Results
• Book your free session by visiting www.lernova.co.uk" or something similar to that.
• Contact Details:
• 020 7418 2903
• enquiries@lernova.co.uk
• Address (*with map*):
• Corbel Business and Innovation Centre
• Wyvern Court
• Larkfield Road
• HA9 4QW
Nice to have
• similar colour scheme as the logo. creative background design.

```html
<!DOCTYPE html>
<html lang="en">
<head>
<meta charset="utf-8">
<title>Private Maths Tuition – A5 Flyer</title>
<link rel="stylesheet" href="https://fonts.googleapis.com/css2?family=Arimo:wght@400;700&display=swap">
<style>
  :root {
    --brand-blue: #1557a6;
    --brand-navy: #0d3f8f;
    --brand-orange: #f07125;
    --brand-green: #9bc83c;
    --ink: #111111;
    --paper: #ffffff;
    --stage: #1a1a1a;
    --map-tone: #e7e3dc;
    --map-park: #cfe0b4;
  }
  * { box-sizing: border-box; margin: 0; padding: 0; }
  html, body {
    width: 1200px; height: 1200px; overflow: hidden;
    background: var(--stage);
    font-family: "Arimo", Arial, sans-serif;
  }
  .flyer {
    position: absolute; left: 204px; top: 40px;
    width: 792px; height: 1120px;
    background: var(--paper); overflow: hidden;
  }
  .flyer__bands { position: absolute; inset: 0; width: 100%; height: 100%; }
  .top-stripe { position: absolute; left: 0; top: 0; height: 21px; width: 100%; display: flex; }
  .top-stripe__orange { flex: 0 0 651px; background: var(--brand-orange); }
  .top-stripe__green { flex: 1; background: var(--brand-green); }
  .header {
    position: absolute; left: 0; top: 21px; width: 100%; height: 127px;
    background: var(--brand-blue);
    display: flex; align-items: center; justify-content: center;
  }
  .header__title { color: var(--paper); font-weight: 700; font-size: 70px; letter-spacing: -0.5px; }
  .subtitle {
    position: absolute; left: 0; top: 160px; width: 100%; text-align: center;
    color: var(--brand-orange); font-weight: 700; font-size: 36px;
  }
  .brand {
    position: absolute; left: 74px; top: 300px;
    display: flex; align-items: center; gap: 12px;
  }
  .brand__dot { width: 22px; height: 22px; border-radius: 50%; background: var(--brand-green); }
  .brand__name { color: var(--brand-orange); font-weight: 400; font-size: 54px; }
  .students-photo {
    position: absolute; left: 378px; top: 210px; width: 396px; height: 570px;
    background: linear-gradient(180deg, #f3f1ee 0%, #dfe4ec 45%, #8ca6c9 75%, #f3f1ee 100%);
    border-radius: 4px;
  }
  .offer {
    position: absolute; left: 66px; top: 399px; width: 339px; height: 143px;
    background: var(--brand-green);
    clip-path: polygon(0 0, 100% 0, 100% 82%, 92% 100%, 0 100%);
    padding: 22px 0 0 34px;
    color: var(--paper); font-weight: 700; font-size: 46px; line-height: 53px;
  }
  .benefits {
    position: absolute; left: 100px; top: 566px; list-style: none;
    color: var(--ink); font-size: 18px; line-height: 29.7px;
  }
  .location-map {
    position: absolute; left: 77px; top: 719px; width: 297px; height: 308px;
    border-top: 4px solid var(--brand-blue);
    background: linear-gradient(135deg, var(--map-tone) 0%, var(--map-tone) 55%, var(--map-park) 100%);
  }
  .booking { position: absolute; left: 77px; top: 1027px; width: 297px; }
  .booking__lead {
    height: 32px; background: var(--brand-orange); color: var(--paper);
    font-size: 17px; display: flex; align-items: center; justify-content: center;
  }
  .booking__url {
    height: 61px; background: var(--brand-blue); color: var(--paper);
    font-weight: 700; font-size: 20px; text-align: center; padding-top: 9px;
  }
  .contact {
    position: absolute; left: 442px; top: 898px;
    color: var(--ink); font-size: 15.5px; line-height: 19.5px;
  }
  .contact__label { color: var(--brand-navy); font-weight: 700; }
  .contact__group + .contact__group { margin-top: 19px; }
</style>
</head>
<body>
<main class="flyer">
  <svg class="flyer__bands" viewBox="0 0 740 1043" preserveAspectRatio="none" aria-hidden="true">
    <polygon fill="#f07125" points="0,642 520,766 740,742 740,808 525,803 0,668"/>
    <polygon fill="#9bc83c" points="0,668 525,803 740,808 740,870 0,684"/>
  </svg>

  <div class="top-stripe"><span class="top-stripe__orange"></span><span class="top-stripe__green"></span></div>
  <header class="header"><h1 class="header__title">Private Maths Tuition</h1></header>
  <p class="subtitle">GCSE, A-Levels. 11 Plus Exams</p>

  <div class="brand"><span class="brand__dot"></span><span class="brand__name">Lernova</span></div>

  <div class="students-photo" role="img" aria-label="Photo of four smiling students standing together holding books"></div>

  <div class="offer">FREE FIRST<br>SESSION</div>

  <ul class="benefits">
    <li>Monthly Feedback reports</li>
    <li>Free support outside of sessions</li>
    <li>Clear Target grades</li>
    <li>Personalised Lesson plans</li>
    <li>Tangible Results</li>
  </ul>

  <div class="location-map" role="img" aria-label="Street map showing the location of Corbel Business and Innovation Centre"></div>

  <div class="booking">
    <p class="booking__lead">Book your free session by visiting</p>
    <p class="booking__url">www.lernova.co.uk</p>
  </div>

  <address class="contact" style="font-style:normal">
    <div class="contact__group">
      <p class="contact__label">Contact Details:</p>
      <p>020 7418 2903</p>
      <p>enquiries@lernova.co.uk</p>
    </div>
    <div class="contact__group">
      <p class="contact__label">Address:</p>
      <p>Corbel Business and Innovation Centre</p>
      <p>Wyvern Court</p>
      <p>Larkfield Road</p>
      <p>HA9 4QW</p>
    </div>
  </address>
</main>
</body>
</html>
```